Startup company business card (Media & Advertising)

we need a business card design for a company that is a startup in the media and aggregation industry. Card needs to look funky and of a new breed/modern and upmarket.

Target Market(s)

advertisers/ brand agencies & media publishers

Industry/Entity Type

Advertising

Contact Information for Business Card

Please ensure the front face signifies our brand (plumvexo.com) and back has details for the contact. Standard contact such as phone , address, email , website etc.

Font styles to use
Other font styles liked:
• use styleguide and logo font and color

Colors

Designer to choose colors to be used in the design.

Requirements
Must have
• We are disrupting the media and agency industry so subtlety would be good to use imagery to signify this
Nice to have
• Please use logo colors for branding
Should not have
• be as creative and provide few options. Pick a brand color from logo and styleguide

```html
<!DOCTYPE html>
<html lang="en">
<head>
<meta charset="utf-8">
<title>plumvexo business card</title>
<link rel="stylesheet" href="https://fonts.googleapis.com/css2?family=Oswald:wght@500&family=Roboto:wght@400;700&display=swap">
<style>
  :root {
    --backdrop: #2a2a2a;
    --card: #1c1c1c;
    --logo-ink: #6e6e6e;
    --accent: #e0323f;
    --accent-deep: #b3243f;
    --text-light: #ececec;
    --divider: #d9d9d9;
  }
  * { margin: 0; padding: 0; box-sizing: border-box; }
  html, body { width: 1200px; height: 901px; overflow: hidden; }
  body {
    background: var(--backdrop);
    font-family: "Roboto", Arial, sans-serif;
    position: relative;
  }
  .card {
    position: absolute;
    left: 320px;
    width: 560px;
    height: 320px;
    background: var(--card);
    box-shadow: 0 10px 28px rgba(0,0,0,0.45);
    overflow: hidden;
  }
  .card--front { top: 100px; }
  .card--back { top: 470px; }

  .brand {
    position: absolute;
    left: 0; right: 0; top: 50%;
    transform: translateY(-50%);
    display: flex;
    align-items: center;
    justify-content: center;
    gap: 18px;
  }
  .brand__dot {
    width: 46px; height: 46px;
    border-radius: 50%;
    background: var(--logo-ink);
  }
  .brand__name {
    font-family: "Roboto", Arial, sans-serif;
    font-weight: 700;
    font-size: 52px;
    color: var(--logo-ink);
    letter-spacing: 1px;
  }

  .identity {
    position: absolute;
    right: 300px;
    top: 106px;
    text-align: right;
  }
  .identity__name {
    font-family: "Oswald", "Arial Narrow", sans-serif;
    font-weight: 500;
    font-size: 33px;
    line-height: 1;
    color: var(--accent);
    text-transform: uppercase;
    letter-spacing: 0.5px;
  }
  .identity__role {
    font-size: 17px;
    color: var(--text-light);
    margin-top: 4px;
  }
  .divider {
    position: absolute;
    left: 278px;
    top: 104px;
    width: 2px;
    height: 66px;
    background: var(--divider);
  }
  .contacts {
    position: absolute;
    left: 296px;
    top: 102px;
    list-style: none;
  }
  .contacts li {
    display: flex;
    align-items: center;
    gap: 10px;
    font-size: 17px;
    line-height: 23px;
    color: var(--text-light);
  }
  .contacts svg { width: 14px; height: 14px; flex: none; }
  .address {
    position: absolute;
    left: 0; right: 0;
    top: 252px;
    text-align: center;
    font-size: 17px;
    color: var(--text-light);
  }
  .accent-band {
    position: absolute;
    left: 0; right: 0; bottom: 0;
    height: 11px;
    background: linear-gradient(90deg, var(--accent), var(--accent-deep));
  }
</style>
</head>
<body>
  <section class="card card--front" aria-label="Card front">
    <div class="brand">
      <span class="brand__dot"></span>
      <span class="brand__name">plumvexo</span>
    </div>
  </section>

  <section class="card card--back" aria-label="Card back">
    <div class="identity">
      <p class="identity__name">Marlon Vexley</p>
      <p class="identity__role">Manager</p>
    </div>
    <span class="divider"></span>
    <ul class="contacts">
      <li>
        <svg viewBox="0 0 16 16" aria-hidden="true"><path fill="#e0323f" d="M3.6 1.5l2.3 2.6-1.3 1.6c.9 2 2.5 3.6 4.5 4.6l1.6-1.3 2.6 2.3-1.5 2.2C6.9 13 3 9.1 1.5 3z"/></svg>
        555-318-0427
      </li>
      <li>
        <svg viewBox="0 0 16 16" aria-hidden="true"><rect x="1" y="3" width="14" height="10" fill="#e0323f"/><path d="M1 3l7 6 7-6" fill="none" stroke="#1c1c1c" stroke-width="1.3"/></svg>
        hello@plumvexo.com
      </li>
      <li>
        <svg viewBox="0 0 16 16" aria-hidden="true"><circle cx="8" cy="8" r="6.5" fill="none" stroke="#e0323f" stroke-width="1.6"/><path d="M1.5 8h13M8 1.5c-3 3.5-3 9.5 0 13M8 1.5c3 3.5 3 9.5 0 13" fill="none" stroke="#e0323f" stroke-width="1.2"/></svg>
        www.plumvexo.com
      </li>
    </ul>
    <p class="address">Your address, city, state, ZIP 0000</p>
    <div class="accent-band"></div>
  </section>
</body>
</html>
```